International Travel & Visas Firm needs a Schengen Visa eBook Cover Design

We need an ebook cover design for an online based travel, immigration, visas & nationality law firm called 'OrV' (ordinance and relocation). We are all about helping people overcome the obstacles to travel and ensuring that people achieve their dreams and ambitions through travel to various destinations and bettering their lives.This initial ebook cover is for our downloaded pdf ebook all about Schengen visas and travelling to any of the 26 European countries that form the Schengen Zone.We want people to be excited about buying this book even before receiving it.We would like to see amazing designs that also speak to our logo and new branding.Check out https://ordinanceandrelocation.example/schengen-visas/ and http://ordinanceandrelocation.pages.funnelkit.example/start-your-schengen-visa-application

Target Market(s)

Travellers that want to get a visa to travel around Europe

Industry/Entity Type

Travel Industry

Colors
fbee3d
faa54b

Requirements
Must have
• - Title:
• Schengen Visa Guide
Nice to have
• - tagline:
• Liberate yourself and travel to 26 European Countries
• - OrV Logo
• - Reference to it being an insider's guide to Schengen Visas
• - a play on the word OrV (I am)

```html
<!DOCTYPE html>
<html lang="en">
<head>
<meta charset="utf-8">
<title>Schengen Visa Guide – OrV</title>
<link rel="stylesheet" href="https://fonts.googleapis.com/css2?family=Caveat+Brush&family=Montserrat:wght@400;500&family=Old+Standard+TT:wght@700&display=swap">
<style>
  :root {
    --page: #eceef0;
    --ink: #111111;
    --ink-soft: #3a3a3a;
    --paper: #ffffff;
    --orange: #f07f32;
    --logo-grey: #444444;
  }
  html, body {
    margin: 0;
    padding: 0;
    overflow: hidden;
  }
  .cover {
    position: relative;
    width: 750px;
    height: 1200px;
    background: var(--page);
    overflow: hidden;
  }
  .tagline {
    position: absolute;
    top: 68px;
    left: 0;
    width: 750px;
    text-align: center;
    font-family: "Montserrat", sans-serif;
    font-weight: 400;
    font-size: 20px;
    letter-spacing: 5px;
    color: var(--ink-soft);
    margin: 0;
  }
  .tagline-rule {
    position: absolute;
    top: 127px;
    left: 100px;
    width: 551px;
    height: 2px;
    background: var(--ink-soft);
  }
  .country-count {
    position: absolute;
    top: 155px;
    left: 0;
    width: 750px;
    text-align: center;
    font-family: "Montserrat", sans-serif;
    font-weight: 500;
    font-size: 25px;
    letter-spacing: 6px;
    color: var(--ink-soft);
    margin: 0;
  }
  .slogan {
    position: absolute;
    top: 425px;
    left: 0;
    width: 770px;
    margin: 0;
    text-align: center;
    font-family: "Old Standard TT", serif;
    font-weight: 700;
    color: var(--ink);
    font-size: 44px;
    line-height: 1;
  }
  .slogan-line {
    display: block;
    height: 64px;
  }
  .slogan-highlight {
    display: inline-block;
    background: var(--ink);
    color: var(--paper);
    padding: 2px 8px 4px;
    font-size: 46px;
  }
  .title {
    position: absolute;
    top: 628px;
    left: 0;
    width: 780px;
    margin: 0;
    text-align: center;
    font-family: "Caveat Brush", cursive;
    font-weight: 400;
    color: var(--orange);
    font-size: 122px;
    line-height: 108px;
  }
  .title-line {
    display: block;
  }
  .brand {
    position: absolute;
    top: 1018px;
    left: 0;
    width: 750px;
    display: flex;
    align-items: center;
    justify-content: center;
    gap: 14px;
  }
  .brand-mark {
    width: 22px;
    height: 22px;
    background: var(--orange);
  }
  .brand-name {
    font-family: "Old Standard TT", serif;
    font-weight: 700;
    font-size: 84px;
    line-height: 1;
    color: var(--logo-grey);
  }
  .brand-descriptor {
    position: absolute;
    top: 1133px;
    left: 0;
    width: 750px;
    text-align: center;
    font-family: "Old Standard TT", serif;
    font-weight: 700;
    font-size: 16px;
    color: var(--ink-soft);
    margin: 0;
  }
</style>
</head>
<body>
<main class="cover">
  <p class="tagline">LIBERATE YOURSELF AND TRAVEL TO</p>
  <div class="tagline-rule"></div>
  <p class="country-count">• 26 EUROPEAN COUNTRIES •</p>

  <h2 class="slogan">
    <span class="slogan-line">I AM AN</span>
    <span class="slogan-line"><span class="slogan-highlight">IMMIGRANT</span></span>
    <span class="slogan-line">ARE YOU?</span>
  </h2>

  <h1 class="title">
    <span class="title-line">Schengen</span>
    <span class="title-line">Visa</span>
    <span class="title-line">Guide</span>
  </h1>

  <div class="brand">
    <span class="brand-mark"></span>
    <span class="brand-name">OrV</span>
  </div>
  <p class="brand-descriptor">ordinance and relocation</p>
</main>
</body>
</html>
```